Marijuana Lifestyle Multi-Shop Brand Website

We need a website that provides an online retail shop for our products, along with the additional functionality:

Main Page: Slider with great photography (we are still looking for a professional photographer to take photos for us.

Shop Tab: E-commerce site.
- Main Categories:
- Accessories
- Bubblers
- Dry Pieces
- Scientific Glass
- Water Pipes
- Custom Shop
- University Store

Stores/Resellers: This is a store look-up, so people can enter their zipcode and find our resellers and partners.

Brand Partners: Just a basic filter and page so that we can highlight our partners and why we've selected them.

Contact Us: Basic Form
- Career Page: Basic Page

About Us: Basic Page

Blog:

Search Bar:

Essentially, we want a near exact copy of this website, but with our brand, logo and content. https://plumcratevault.com/

This site is really really simple, but we like simple.

Our reserved domain address is: www.runsowmend.com

About Us:
We are multi-shop for marijuana-related accessories. We sell quality glass pipes, vaporizers, amazing storage options, dime bags, custom t-shirts and other stuff.

We have a network of resellers that allow us to put in micro-installations into gift shops, convenience stores, tobacco stores, etc. and we are trying to change the overall perception that buying these items should be mainstream and as transparent as going to the Elk or the Birch Depot.

I've attached a logo that should give you an idea of our color scheme. We don't have our photography yet for the slider

As an FYI, for the e-commerce part of my website, I already have a license for WP SwiftTill.

```html
<!DOCTYPE html>
<html lang="en">
<head>
<meta charset="utf-8">
<title>About Us – Kindred Leaf</title>
<link href="https://fonts.googleapis.com/css2?family=Arimo:wght@400;700&family=Cabin:wght@700&display=swap" rel="stylesheet">
<style>
  :root{
    --stage:#000000;
    --topbar:#242424;
    --header:#1e1e1e;
    --titlebar:#1a1a1a;
    --main:#1c1c1c;
    --line:#333333;
    --text:#e6e6e6;
    --muted:#8c8c8c;
    --nav:#9a9a9a;
    --accent:#8eab1c;
    --accent-dark:#3f5114;
    --icon-bg:#333333;
    --white:#ffffff;
  }
  *{box-sizing:border-box;margin:0;padding:0}
  html,body{width:1200px;height:1000px;overflow:hidden;background:var(--stage)}
  body{position:relative;font-family:"Arimo",Arial,sans-serif;color:var(--text)}
  .site{position:absolute;left:0;top:163px;width:1190px;height:677px;background:var(--main)}

  .topbar{position:absolute;left:0;top:0;width:100%;height:24px;background:var(--topbar);border-bottom:1px solid var(--line)}
  .social{position:absolute;left:200px;top:0;display:flex;height:23px}
  .social span{width:23px;height:23px;border-right:1px solid var(--line);display:flex;align-items:center;justify-content:center}
  .social span::after{content:"";width:5px;height:5px;border-radius:50%;background:#777}
  .social span:first-child{border-left:0}
  .meta-nav{position:absolute;right:209px;top:0;height:23px;display:flex;align-items:center;font-size:8px;font-weight:700;color:var(--nav)}
  .meta-nav a{color:var(--nav);text-decoration:none;padding:0 8px;border-right:1px solid #4a4a4a;line-height:10px}
  .meta-nav a.current{color:var(--white)}
  .meta-nav .contact{padding-left:8px}

  .header{position:absolute;left:0;top:24px;width:100%;height:87px;background:var(--header);border-bottom:1px solid var(--line)}
  .brand{position:absolute;left:211px;top:10px;display:flex;align-items:center;gap:10px}
  .brand-mark{width:64px;height:64px;border-radius:50%;background:var(--accent-dark)}
  .brand-name{font-family:"Arimo",Arial,sans-serif;font-size:24px;font-weight:700;color:#b9cf6a;line-height:1}
  .main-nav{position:absolute;right:212px;top:0;height:86px;display:flex;align-items:center;font-size:10.5px}
  .main-nav a{color:var(--nav);text-decoration:none;margin-left:20px;position:relative;height:86px;display:flex;align-items:center;padding:0 0}
  .main-nav a.current{color:var(--white);padding:0 10px;margin-left:10px}
  .main-nav a.current::after{content:"";position:absolute;left:0;right:0;bottom:-1px;height:3px;background:var(--accent)}
  .main-nav .search{margin-left:20px;display:flex}

  .titlebar{position:absolute;left:0;top:111px;width:100%;height:44px;background:var(--titlebar);border-bottom:1px solid var(--line)}
  .page-title{position:absolute;left:207px;top:14px;font-size:12px;color:var(--white)}
  .breadcrumb{position:absolute;right:211px;top:17px;font-size:8px;color:#bbb}

  .intro{position:absolute;left:207px;top:203px;width:364px;font-size:10.3px;line-height:15.8px;text-align:justify}
  .intro p{margin-bottom:8px}
  .hl{color:var(--accent);font-weight:700}
  .soft{color:var(--accent);font-style:italic}
  .dropcap{float:left;font-size:28px;line-height:22px;color:var(--white);margin:4px 6px 0 0}
  .badge{float:left;width:118px;height:118px;border-radius:50%;background:var(--accent-dark);margin:-2px 7px 4px 0;display:flex;align-items:center;justify-content:center;font-size:13px;font-weight:700;color:#b9cf6a}
  .divider{position:absolute;left:330px;top:442px;width:117px;height:1px;background:#444}
  .divider::after{content:"";position:absolute;left:54px;top:-3px;width:7px;height:7px;border-radius:50%;border:1px solid #555;background:var(--main)}
  .story{top:474px}

  .features{position:absolute;left:630px;top:214px;width:349px}
  .feature-line{position:absolute;left:956px;top:240px;height:300px;border-left:1px dotted #555}
  .feature{position:absolute;right:0;width:349px;height:80px}
  .feature h3{position:absolute;right:70px;top:2px;font-family:"Cabin",Arial,sans-serif;font-size:13px;font-weight:700;color:var(--white);letter-spacing:.2px}
  .feature p{position:absolute;right:70px;top:23px;width:280px;text-align:right;font-size:10.3px;line-height:15.8px;color:var(--muted)}
  .feature .icon{position:absolute;right:0;top:0;width:48px;height:48px;border-radius:50%;background:var(--icon-bg);display:flex;align-items:center;justify-content:center}
</style>
</head>
<body>
<div class="site">
  <div class="topbar">
    <div class="social"><span></span><span></span><span></span><span></span><span></span><span></span></div>
    <nav class="meta-nav">
      <a>HOME</a><a class="current">About Us</a><a>My Account</a><a>Shop</a><a>Career Page</a><a>Blog</a><a>Contact Us</a>
      <span class="contact">+1 800 555 0199 / info@runsowmend.com</span>
    </nav>
  </div>

  <header class="header">
    <div class="brand"><div class="brand-mark"></div><div class="brand-name">Kindred Leaf</div></div>
    <nav class="main-nav">
      <a>HOME</a><a class="current">About Us</a><a>My Account</a><a>Shop</a><a>Career Page</a><a>Blog</a><a>Contact Us</a>
      <span class="search"><svg width="10" height="10" viewBox="0 0 10 10"><circle cx="4" cy="4" r="3" fill="none" stroke="#9a9a9a" stroke-width="1.4"/><line x1="6.2" y1="6.2" x2="9.3" y2="9.3" stroke="#9a9a9a" stroke-width="1.6"/></svg></span>
    </nav>
  </header>

  <div class="titlebar">
    <h1 class="page-title">About Us</h1>
    <div class="breadcrumb">You are here:&nbsp; Home &nbsp;/&nbsp; About Us</div>
  </div>

  <section class="intro">
    <div class="badge">Kindred Leaf</div>
    <p><span class="dropcap">L</span>orem ipsum dolor sit amet, <span class="hl">consectetur adipiscing elit.</span> Vestibulum ac vestibulum massa, nec dignissim tellus. Donec vitae volutpat ligula. Phasellus viverra lectus diam. Praesent vehicula neque non odio lobortis consectetur. <span class="hl">Fusce eleifend risus dolor, nec rhoncus leo auctor sit amet.</span> Nunc convallis lectus libero, auctor laoreet ante tincidunt quis. Sed est massa, <span class="hl">pellentesque vitae adipiscing at</span>, feugiat sed turpis. Morbi consequat sodales augue quis ornare.</p>
    <p><span class="hl">Lorem ipsum dolor sit amet, consectetur adipiscing elit. Vestibulum ac vestibulum massa, nec dignissim tellus.</span> Donec vitae volutpat ligula. Phasellus viverra lectus diam. Praesent vehicula neque non odio lobortis consectetur. Fusce eleifend risus dolor, <span class="soft">nec rhoncus leo auctor sit amet</span>.</p>
  </section>

  <div class="divider"></div>

  <section class="intro story">
    <p><span class="dropcap">L</span>orem ipsum dolor sit amet, <span class="hl">consectetur adipiscing elit.</span> Vestibulum ac vestibulum massa, nec dignissim tellus. Donec vitae volutpat ligula. Phasellus viverra lectus diam. Praesent vehicula neque non odio lobortis consectetur. <span class="hl">Fusce eleifend risus dolor, nec rhoncus leo auctor sit amet.</span> Nunc convallis lectus libero, auctor laoreet ante tincidunt quis. Sed est massa, <span class="hl">pellentesque vitae adipiscing at</span>, feugiat sed turpis. Morbi consequat sodales augue quis ornare.</p>
    <p><span class="hl">Lorem ipsum dolor sit amet, consectetur adipiscing elit. Vestibulum ac vestibulum massa, nec dignissim tellus.</span> Donec vitae volutpat ligula. Phasellus viverra lectus diam. Praesent vehicula neque non odio lobortis consectetur. Fusce eleifend risus dolor, <span class="soft">nec rhoncus leo auctor sit amet</span>.</p>
  </section>

  <div class="feature-line"></div>
  <section class="features">
    <article class="feature" style="top:0">
      <h3>LIST TITLE 1</h3>
      <p>Lorem ipsum dolor sit amet, consectetur adipiscing elit. Vestibulum ac vestibulum massa, nec dignissim tellus. Donec vitae volutpat ligula. Phasellus viverra lectus diam.</p>
      <div class="icon"><svg width="20" height="20" viewBox="0 0 20 20"><path d="M3 17l1-4 9-9 3 3-9 9z" fill="#fff"/><path d="M14 3l1.5-1.5 3 3L17 6z" fill="#fff"/></svg></div>
    </article>
    <article class="feature" style="top:101px">
      <h3>LIST TITLE 2</h3>
      <p>Lorem ipsum dolor sit amet, consectetur adipiscing elit. Vestibulum ac vestibulum massa, nec dignissim tellus. Donec vitae volutpat ligula. Phasellus viverra lectus diam.</p>
      <div class="icon"><svg width="20" height="20" viewBox="0 0 20 20"><path d="M10 17L3 10A4 4 0 0 1 10 5a4 4 0 0 1 7 5z" fill="#fff"/></svg></div>
    </article>
    <article class="feature" style="top:202px">
      <h3>LIST TITLE 3</h3>
      <p>Lorem ipsum dolor sit amet, consectetur adipiscing elit. Vestibulum ac vestibulum massa, nec dignissim tellus. Donec vitae volutpat ligula. Phasellus viverra lectus diam.</p>
      <div class="icon"><svg width="20" height="20" viewBox="0 0 20 20"><rect x="3" y="9" width="3" height="8" fill="#fff"/><path d="M7 9l3-6c1.5 0 2 1 1.5 2.5L11 8h5c1 0 1.5 1 1.2 2l-1.5 6c-.2.7-.8 1-1.5 1H7z" fill="#fff"/></svg></div>
    </article>
    <article class="feature" style="top:303px">
      <h3>LIST TITLE 4</h3>
      <p>Lorem ipsum dolor sit amet, consectetur adipiscing elit. Vestibulum ac vestibulum massa, nec dignissim tellus. Donec vitae volutpat ligula. Phasellus viverra lectus diam.</p>
      <div class="icon"><svg width="20" height="20" viewBox="0 0 20 20"><rect x="10" y="2" width="2" height="13" fill="#fff"/><ellipse cx="8" cy="15.5" rx="3.5" ry="2.7" fill="#fff"/><path d="M12 2c1 3 5 4 4 8-1-2-2.5-3-4-3z" fill="#fff"/></svg></div>
    </article>
  </section>
</div>
</body>
</html>
```